Coffee to go business card

Can you make an Orange card please.
our other colours are black chocolate and white for the writing.
If you could make the name and phone number more prominant.

Target Market(s)

People on the go.

Industry/Entity Type

Business

Contact Information for Business Card

Tarvo Espresso Bar - coffee to go
Open at the Orange window
Weekdays 5.30am to 2.30pm
Saturdays 7.30am to 2.00pm
Phone orders welcome 47918306
Shop 9 Linden Vale Centre
17 Barrow Street, Linden VAle, 4865
Serving Fresh Vasko Espresso
Like us on friendbook

Requirements
Must have
• I have attached our logo but not dure if it uploaded correctly?
Nice to have
• see above

```html
<!DOCTYPE html>
<html lang="en">
<head>
<meta charset="utf-8">
<title>Tarvo Espresso Bar – Business Card</title>
<link rel="stylesheet" href="https://fonts.googleapis.com/css2?family=Lora:ital,wght@1,400&display=swap">
<style>
  :root {
    --page: #efe3d8;
    --card-orange: #f9a51b;
    --chocolate-soft: rgba(107, 58, 30, 0.5);
    --chocolate-faint: rgba(107, 58, 30, 0.28);
    --chocolate-clear: rgba(107, 58, 30, 0);
    --text-white: #ffffff;
    --text-shadow: rgba(60, 28, 8, 0.75);
  }
  * { margin: 0; padding: 0; box-sizing: border-box; }
  html, body {
    width: 1200px;
    height: 1000px;
    overflow: hidden;
    background: var(--page);
  }
  .canvas {
    position: relative;
    width: 1200px;
    height: 1000px;
  }
  .card {
    position: absolute;
    left: 219px;
    width: 762px;
    height: 428px;
    background: var(--card-orange);
    border-radius: 22px;
    overflow: hidden;
    font-family: "Lora", Georgia, serif;
    font-style: italic;
    font-weight: 400;
    color: var(--text-white);
    text-align: center;
    text-shadow: 2px 2px 3px var(--text-shadow);
  }
  .card--front { top: 48px; }
  .card--back { top: 524px; }
  .cup-art {
    position: absolute;
    border-radius: 46% 46% 50% 50%;
    background: radial-gradient(ellipse at 50% 55%, var(--chocolate-soft) 0%, var(--chocolate-faint) 45%, var(--chocolate-clear) 72%);
  }
  .card--front .cup-art { left: 195px; top: 62px; width: 390px; height: 370px; }
  .card--back .cup-art { left: 190px; top: 18px; width: 400px; height: 400px; }
  .text-block {
    position: absolute;
    left: 0;
    right: 0;
    font-weight: 400;
    white-space: nowrap;
  }
  .business-name {
    top: 22px;
    font-size: 60px;
    line-height: 1;
    padding-left: 16px;
  }
  .tagline {
    top: 96px;
    font-size: 32px;
    line-height: 1;
    padding-right: 24px;
  }
  .hours {
    top: 282px;
    font-size: 36px;
    line-height: 34px;
  }
  .phone {
    top: 36px;
    font-size: 38px;
    line-height: 1;
    padding-left: 18px;
  }
  .address {
    top: 128px;
    font-size: 38px;
    line-height: 34px;
  }
  .promo {
    top: 322px;
    font-size: 38px;
    line-height: 34px;
  }
</style>
</head>
<body>
<main class="canvas">
  <section class="card card--front">
    <div class="cup-art" role="img" aria-label="Illustration of a steaming coffee cup in chocolate brown tones"></div>
    <h1 class="text-block business-name">Tarvo Espresso Bar</h1>
    <p class="text-block tagline">- coffee to go -</p>
    <p class="text-block hours">Weekdays :5.30am to 2.30pm<br>Saturdays :7.30am to 2.00pm<br>~Open at the Orange window~</p>
  </section>
  <section class="card card--back">
    <div class="cup-art" role="img" aria-label="Illustration of a steaming coffee cup in chocolate brown tones"></div>
    <p class="text-block phone">Phone orders :47918306</p>
    <p class="text-block address">Shop 9 : Linden Vale Centre<br>17 Barrow Street,<br>Linden VAle<br>4865</p>
    <p class="text-block promo">Serving Fresh Vasko Espresso!<br>Like us on friendbook!</p>
  </section>
</main>
</body>
</html>
```